Brimvale Crest Homes needs a business card

We need a business card for a new company in Canada, Ontario. Our company is all about luxury contraction homes for our clients. Our product and services are custom projects design. Under the business logo that will be created, we want a slogan that will be a memorable phrase for consumers to remember us to tell their friends and relatives.

Additional infomation
- Teodoro Vanlesky
- President / Ceo
-519.304.7718

Find point what luxury construction products and services can be done

We like to see colors:
- #663300
- and something other colors or color that would attract the client needs and wants

The final design should communicate leads from new or old clients that will grow our empire. Most of all, we try to work among the budget that clients want

NOTE
- we also need an icon for the business (Example: Instagram, Facebook, and Whatsapp icons)
- We want the company name to be remembered easily for clients and our distributors who would get our orders.
- we need an icon on the business cards: Facebook and Instagram.

Thanks,
Brimvale Crest Homes

```html
<!DOCTYPE html>
<html lang="en">
<head>
<meta charset="utf-8">
<title>Brimvale Crest Homes – Business Card</title>
<link href="https://fonts.googleapis.com/css2?family=Work+Sans:wght@400;500;600;800&display=swap" rel="stylesheet">
<style>
  :root {
    --brand-brown: #663300;
    --card-brown: #6a3a1a;
    --ink-grey: #555555;
    --paper: #ffffff;
    --backdrop: #1c1c1c;
  }
  * { box-sizing: border-box; margin: 0; padding: 0; }
  html, body {
    width: 1200px; height: 900px; overflow: hidden;
    background: var(--backdrop);
    font-family: "Work Sans", Arial, sans-serif;
  }
  .canvas {
    position: relative; width: 1200px; height: 900px;
    display: flex; flex-direction: column; align-items: center; justify-content: center; gap: 40px;
  }
  .card {
    position: relative; width: 560px; height: 320px; overflow: hidden;
  }
  /* Back side */
  .card-back {
    background: var(--card-brown);
    display: flex; align-items: center; justify-content: center;
  }
  .wordmark { text-align: center; color: var(--paper); }
  .wordmark-name {
    font-weight: 800; font-size: 38px; letter-spacing: 0.5px; line-height: 1;
  }
  .wordmark-tagline {
    font-weight: 600; font-size: 11.5px; letter-spacing: 0.6px; margin-top: 6px;
  }
  /* Front side */
  .card-front { background: var(--paper); }
  .front-logo {
    position: absolute; top: 34px; right: 34px; text-align: center; color: var(--brand-brown);
  }
  .front-logo .wordmark-name { font-size: 24px; }
  .front-logo .wordmark-tagline { font-size: 7.5px; margin-top: 4px; letter-spacing: 0.3px; }
  .holder { position: absolute; left: 40px; top: 128px; }
  .holder-name { color: var(--brand-brown); font-weight: 600; font-size: 22px; }
  .holder-title { color: var(--ink-grey); font-size: 14px; margin-top: 2px; letter-spacing: 0.5px; }
  .divider {
    position: absolute; left: 40px; right: 40px; top: 192px; height: 1px; background: var(--brand-brown);
  }
  .contacts { position: absolute; left: 40px; top: 206px; list-style: none; }
  .contacts li {
    display: flex; align-items: center; gap: 8px;
    color: var(--ink-grey); font-size: 14px; line-height: 21px; letter-spacing: 0.4px;
  }
  .contacts svg { width: 10px; height: 10px; flex: none; }
  .address {
    position: absolute; right: 40px; top: 238px; text-align: right;
    color: var(--ink-grey); font-size: 14.5px; line-height: 21px; letter-spacing: 0.6px;
  }
  .footer-band { position: absolute; left: 0; bottom: 0; width: 560px; height: 40px; }
</style>
</head>
<body>
<main class="canvas">
  <section class="card card-back" aria-label="Card back">
    <div class="wordmark">
      <div class="wordmark-name">Brimvale Crest Homes</div>
      <div class="wordmark-tagline">- HOME RENOVATIONS - CUSTOM PROJECT DESIGN -</div>
    </div>
  </section>

  <section class="card card-front" aria-label="Card front">
    <div class="wordmark front-logo">
      <div class="wordmark-name">Brimvale Crest Homes</div>
      <div class="wordmark-tagline">- HOME RENOVATIONS - CUSTOM PROJECT DESIGN -</div>
    </div>

    <div class="holder">
      <div class="holder-name">Teodoro Vanlesky</div>
      <div class="holder-title">President / Ceo</div>
    </div>

    <div class="divider"></div>

    <ul class="contacts">
      <li>
        <svg viewBox="0 0 10 10" aria-hidden="true"><path d="M2 1 L4 1 L4.5 3 L3.3 3.8 Q4.3 6 6.2 6.8 L7 5.6 L9 6 L9 8 Q5 9 2.5 6 Q1 4 2 1Z" fill="#663300"/></svg>
        519.304.7718
      </li>
      <li>
        <svg viewBox="0 0 10 10" aria-hidden="true"><rect x="0.7" y="2" width="8.6" height="6" fill="none" stroke="#663300" stroke-width="1"/><path d="M0.7 2 L5 5.5 L9.3 2" fill="none" stroke="#663300" stroke-width="1"/></svg>
        info@brimvalecrest.com
      </li>
      <li>
        <svg viewBox="0 0 10 10" aria-hidden="true"><circle cx="5" cy="5" r="4.2" fill="none" stroke="#663300" stroke-width="0.9"/><ellipse cx="5" cy="5" rx="1.8" ry="4.2" fill="none" stroke="#663300" stroke-width="0.8"/><path d="M0.8 5 H9.2 M1.5 3 H8.5 M1.5 7 H8.5" stroke="#663300" stroke-width="0.7"/></svg>
        www.brimvalecrest.com
      </li>
    </ul>

    <div class="address">88 Harlow Street<br>Guelph, ON N1H 2K7</div>

    <svg class="footer-band" viewBox="0 0 560 40" aria-hidden="true">
      <path d="M0 2 H285 Q300 2 300 8 L0 8 Z" fill="var(--brand-brown)"/>
      <path d="M0 14 H280 Q300 14 318 7 Q330 3 345 3 H560 V40 H0 Z" fill="var(--brand-brown)"/>
    </svg>
  </section>
</main>
</body>
</html>
```